Business Card Design Project

I am a psychotherapist, counselor and expressive arts therapist (means I use every art form imaginable in the service of healing). I'm just starting out in private practice in San Francisco, CA. I work with individual adults, children and families. I'd like the card to mirror the simplicity and color palate of my website. I also would love if there is a symbol, image of fire, flame or spark (that is warming, not frightening).

Check out my website: www.lorabeckettmft.com

I want the cards to be printed in letter press so please keep that in mind!

Target Market(s)

Upper Middle Class Adults who are progressively minded, artistic or artists, open to psychotherapy, interested in health & healing.

Industry/Entity Type

Business

Requirements
Must have
• Text to be included:

Lora Beckett
Counseling, Psychotherapy & Expressive Arts

2814 Wexford Avenue, Suite F
San Francisco, CA 94127
p. 415.862.3097
lorajanebeckett@mailvane.net

www.lorabeckettmft.com

MFT License Number 68947

It's OK to abbreviate Number to # or Street to St., etc.

Must be compatible with letter press printing.
Nice to have
• I don't have a logo. I don't expect designers to necessarily create one for me, but if someone comes up with a simple image (see above about flame), that would be great. I don't have much of a budget now, but expect that to change in the next year or so and then could buy a logo for my website, future letterhead, etc.

```html
<!DOCTYPE html>
<html lang="en">
<head>
<meta charset="utf-8">
<title>Lora Beckett — Business Card</title>
<link href="https://fonts.googleapis.com/css2?family=Mulish:ital,wght@0,400;0,700;1,400&display=swap" rel="stylesheet">
<style>
  :root {
    --backdrop: #34302f;
    --card: #fde0c5;
    --accent: #e8415a;
    --ink: #4a3a3a;
    --flame-top: #f6a72a;
    --flame-mid: #ec6b55;
    --flame-low: #e8455f;
    --pill-text: #fde7e4;
  }
  * { margin: 0; padding: 0; box-sizing: border-box; }
  html, body {
    width: 1200px;
    height: 900px;
    overflow: hidden;
    background: var(--backdrop);
  }
  .card {
    position: absolute;
    left: 100px;
    top: 174px;
    width: 1000px;
    height: 552px;
    background: var(--card);
    border-radius: 34px;
    font-family: "Mulish", sans-serif;
    color: var(--ink);
    overflow: hidden;
  }
  .identity {
    position: absolute;
    left: 75px;
    top: 68px;
  }
  .identity .name {
    font-weight: 700;
    font-size: 41px;
    color: var(--accent);
    line-height: 1.1;
    letter-spacing: 0.2px;
  }
  .identity .practice {
    margin-top: 6px;
    font-style: italic;
    font-size: 27px;
    line-height: 33px;
  }
  .contact {
    position: absolute;
    left: 75px;
    top: 337px;
    list-style: none;
    font-size: 27px;
    line-height: 33px;
  }
  .contact li {
    display: flex;
    align-items: center;
  }
  .contact .icon {
    width: 20px;
    height: 20px;
    margin-right: 14px;
    flex: none;
    fill: var(--accent);
  }
  .contact .indent { padding-left: 34px; }
  .flame-art {
    position: absolute;
    left: 553px;
    top: 47px;
    width: 410px;
    height: 505px;
    border-radius: 60% 60% 0 0 / 75% 75% 0 0;
    background: linear-gradient(to bottom, var(--flame-top) 0%, var(--flame-mid) 30%, var(--flame-low) 62%, rgba(232, 69, 95, 0) 100%);
    opacity: 0.85;
  }
  .license {
    position: absolute;
    left: 645px;
    top: 472px;
    width: 219px;
    height: 32px;
    border-radius: 16px;
    background: var(--accent);
    color: var(--pill-text);
    font-size: 17px;
    line-height: 32px;
    text-align: center;
  }
</style>
</head>
<body>
  <div class="card">
    <div class="identity">
      <h1 class="name">Lora Beckett</h1>
      <p class="practice">Counseling, Psychotherapy<br>&amp; Expressive Arts</p>
    </div>

    <ul class="contact">
      <li>
        <svg class="icon" viewBox="0 0 20 20" aria-hidden="true"><path d="M10 1a6.5 6.5 0 0 0-6.5 6.5C3.5 12.5 10 19 10 19s6.5-6.5 6.5-11.5A6.5 6.5 0 0 0 10 1zm0 9a2.5 2.5 0 1 1 0-5 2.5 2.5 0 0 1 0 5z"/></svg>
        2814 Wexford Avenue, Suite F
      </li>
      <li class="indent">San Francisco, CA 94127</li>
      <li>
        <svg class="icon" viewBox="0 0 20 20" aria-hidden="true"><circle cx="10" cy="10" r="9"/><path d="M7 5.5l1.6 2.2-1 1.2c.7 1.4 1.8 2.5 3.2 3.2l1.2-1 2.2 1.6-1 1.8c-3.7-.4-6.8-3.5-7.2-7.2z" fill="#fde0c5"/></svg>
        415 862 3097
      </li>
      <li>
        <svg class="icon" viewBox="0 0 20 20" aria-hidden="true"><path d="M2 5h16v10H2z"/><path d="M2 5l8 6 8-6" fill="none" stroke="#fde0c5" stroke-width="1.6"/></svg>
        lorajanebeckett@mailvane.net
      </li>
      <li>
        <svg class="icon" viewBox="0 0 20 20" aria-hidden="true"><circle cx="10" cy="10" r="9"/><g fill="none" stroke="#fde0c5" stroke-width="1.2"><ellipse cx="10" cy="10" rx="3.6" ry="8.4"/><path d="M1.5 10h17M3 5.5h14M3 14.5h14"/></g></svg>
        www.lorabeckettmft.com
      </li>
    </ul>

    <div class="flame-art" role="img" aria-label="Warm flame illustration in orange and pink, fading into the card at the bottom"></div>

    <div class="license">MFT License # 68947</div>
  </div>
</body>
</html>
```